Email signature and business card

Australian company called Brisawa. We provide construction and maintenance services to the mining industry. I would like the design to be similar to our website theme(www.brisawa.com.au) whilst staying compact. RGB colours to include: 42,96,140 and 232,163,0 and I have attached 2 logos.

The following fields will need to be included:

Full Name
Title
Location/Project
Phone
Mobile
Fax
Email
Web site

Target Market(s)

Mining Industry

Industry/Entity Type

Construction

Requirements
Must have
• Full Name, Title, Office Address, Phone, Mobile, Fax, Email, Web address
• Back of card must include: Boilermaking, Carpentry, Concrete, Construction, Cranes, Data and Comms, Electrical, Fabrication, Fitting, Labour Hire, Plumbing, Rigging, Shutdowns

```html
<!DOCTYPE html>
<html lang="en">
<head>
<meta charset="utf-8">
<title>Brisawa Email Signature</title>
<link href="https://fonts.googleapis.com/css2?family=Arimo:ital,wght@0,400;0,700;1,400&display=swap" rel="stylesheet">
<style>
  :root {
    --page: #ffffff;
    --brand-gold: #f5b400;
    --band-dark: #1f4455;
    --band-light: #deebf2;
    --label: #2b4a5e;
    --ink: #111111;
  }
  html, body {
    margin: 0;
    padding: 0;
    width: 1200px;
    height: 1000px;
    overflow: hidden;
    background: var(--page);
    font-family: "Arimo", Arial, sans-serif;
  }
  .signature {
    position: absolute;
    left: 318px;
    top: 455px;
    width: 600px;
    height: 115px;
  }
  .signature__header {
    position: relative;
    height: 41px;
  }
  .brand {
    position: absolute;
    left: 10px;
    top: 12px;
    display: flex;
    align-items: center;
    gap: 7px;
  }
  .brand__square {
    width: 10px;
    height: 10px;
    background: var(--brand-gold);
  }
  .brand__name {
    font-weight: 400;
    font-size: 15px;
    color: var(--band-dark);
  }
  .website {
    position: absolute;
    left: 400px;
    top: 20px;
    font-size: 13px;
    font-weight: 700;
    color: var(--brand-gold);
  }
  .signature__rule {
    height: 10px;
    background: var(--band-dark);
  }
  .signature__details {
    position: relative;
    height: 64px;
    background: var(--band-light);
    font-size: 13px;
    line-height: 16px;
    color: var(--ink);
  }
  .details__col {
    position: absolute;
    top: 16px;
  }
  .person { left: 20px; }
  .person__name {
    font-weight: 700;
    color: var(--brand-gold);
  }
  .person__title {
    font-style: italic;
    font-size: 12.5px;
  }
  .phones { left: 145px; }
  .mail-fax { left: 264px; }
  .address { left: 408px; }
  .label {
    font-weight: 700;
    color: var(--label);
  }
</style>
</head>
<body>
  <section class="signature">
    <header class="signature__header">
      <div class="brand">
        <span class="brand__square"></span>
        <span class="brand__name">Brisawa</span>
      </div>
      <div class="website">www.brisawa.com.au</div>
    </header>
    <div class="signature__rule"></div>
    <div class="signature__details">
      <div class="details__col person">
        <div class="person__name">JOHN DOE</div>
        <div class="person__title">Sales Consultant</div>
      </div>
      <div class="details__col phones">
        <div><span class="label">M:</span> (07) 1234 5678</div>
        <div><span class="label">P:</span> (07) 5000 1200</div>
      </div>
      <div class="details__col mail-fax">
        <div><span class="label">E:</span> email@email.com</div>
        <div><span class="label">F:</span> (07) 5000 1299</div>
      </div>
      <div class="details__col address">
        <div>Level 3, 14 Harbour Lane</div>
        <div>Ridgefield QLD 4000</div>
      </div>
    </div>
  </section>
</body>
</html>
```